We need an eye catching logo design and Business Card that portrays our business, which is the cleaning and protecting of stainless steel with an organic non chemical product. This can be separate to the company name or can incorporate it. Maybe even just the company name itself. Company Name is Gleamwise Gleamwise.
Ideal for products exposed to weather elements, ie: balustrading, enclosures, BBQs, we also supply the product so you can do it yourself (DIY).
In addition we would want to include on this card:
1. My Name (Paul Dremmick)
2. Mobile No. (TBA Later)
3. Email address (TBA Later)
4. Web address (TBA Later)
Updates

Please note that we also need suggestions on a logo, as this we do not have this either.

Please note we have update our brief to be more specific.

Thank You.

Paul

Reason: Awaiting for a couple of revised submissions from feedback given.

Target Market(s)

Purchasing officers and government people.

Industry/Entity Type

Steel

Colors

Designer to choose colors to be used in the design.

Requirements
Must have
• 1. Name (Paul Dremmick)
2. Mobile No. (TBA Later)
Should not have
• Should not be to busy looking

```html
<!DOCTYPE html>
<html lang="en">
<head>
<meta charset="utf-8">
<title>Gleamwise Gleamwise – Business Card</title>
<link rel="stylesheet" href="https://fonts.googleapis.com/css2?family=PT+Sans:ital,wght@1,400;1,700&family=Cinzel:wght@400&family=Kaushan+Script&family=Orbitron:wght@800&display=swap">
<style>
  :root {
    --steel-dark: #5f6f70;
    --steel-mid: #a9b8b8;
    --steel-light: #e4ecec;
    --ink-blue: #1a1aff;
    --ink-blue-deep: #0b0bd6;
    --ink-red: #7a0d0d;
    --shadow-dark: rgba(0, 0, 0, 0.55);
  }
  html, body {
    margin: 0;
    padding: 0;
    width: 1200px;
    height: 741px;
    overflow: hidden;
    background: #ffffff;
  }
  .card {
    position: relative;
    width: 1200px;
    height: 741px;
    overflow: hidden;
    background:
      repeating-linear-gradient(0deg, rgba(255,255,255,0.07) 0px, rgba(255,255,255,0.07) 1px, rgba(0,0,0,0.05) 2px, rgba(0,0,0,0) 3px),
      linear-gradient(90deg,
        var(--steel-dark) 0%,
        var(--steel-mid) 7%,
        var(--steel-light) 18%,
        #b9c7c7 30%,
        var(--steel-light) 44%,
        #c7d3d3 58%,
        var(--steel-light) 70%,
        var(--steel-mid) 86%,
        #8a9a9b 100%);
  }
  .identity {
    position: absolute;
    left: 86px;
    top: 34px;
    margin: 0;
  }
  .owner-name {
    margin: 0;
    font: italic 700 40px/1 "PT Sans", sans-serif;
    color: var(--ink-blue);
    text-shadow: 2px 2px 3px var(--shadow-dark);
  }
  .company-name {
    margin: 8px 0 0 2px;
    font: italic 700 22px/1 "PT Sans", sans-serif;
    color: var(--ink-blue);
  }
  .contacts {
    position: absolute;
    right: 119px;
    top: 38px;
    margin: 0;
    padding: 0;
    list-style: none;
    text-align: right;
    font-family: "PT Sans", sans-serif;
    font-style: italic;
    color: var(--ink-blue);
  }
  .contact-number {
    font-weight: 700;
    font-size: 32px;
    line-height: 1;
  }
  .contact-line {
    font-weight: 700;
    font-size: 20px;
    line-height: 24px;
  }
  .contact-number + .contact-line { margin-top: 6px; }
  .uses {
    position: absolute;
    left: 97px;
    top: 178px;
    margin: 0;
    font-family: "Cinzel", serif;
    font-weight: 400;
    color: var(--ink-red);
    text-shadow: 1px 1px 1px rgba(255,255,255,0.6), -1px -1px 1px rgba(0,0,0,0.25);
  }
  .uses-heading {
    margin: 0;
    font-size: 44px;
    font-weight: 400;
    line-height: 1;
    letter-spacing: 1px;
  }
  .uses-list {
    list-style: none;
    margin: 8px 0 0 35px;
    padding: 0;
    font-size: 44px;
    line-height: 54px;
    letter-spacing: 0.5px;
  }
  .diy-note {
    position: absolute;
    left: 0;
    width: 1204px;
    top: 478px;
    margin: 0;
    text-align: center;
    font: 54px/66px "Kaushan Script", cursive;
    color: var(--ink-red);
    text-shadow: 1px 1px 1px rgba(255,255,255,0.5);
  }
  .tagline {
    position: absolute;
    left: 0;
    width: 1194px;
    top: 666px;
    margin: 0;
    text-align: center;
    font: 800 33px/1 "Orbitron", sans-serif;
    letter-spacing: 4px;
    color: var(--ink-blue-deep);
    transform: skewX(-14deg);
    text-shadow: 2px 3px 3px var(--shadow-dark);
  }
</style>
</head>
<body>
  <main class="card">
    <header class="identity">
      <p class="owner-name">Paul Dremmick</p>
      <p class="company-name">Gleamwise Gleamwise</p>
    </header>

    <ul class="contacts">
      <li class="contact-number">[contact no.]</li>
      <li class="contact-line">[email address]</li>
      <li class="contact-line">[web address]</li>
    </ul>

    <section class="uses">
      <h2 class="uses-heading">Ideal for products exposed to weather!</h2>
      <ul class="uses-list">
        <li>&gt;Balustrading,</li>
        <li>&gt;Enclosures,</li>
        <li>&gt;BBQs etc.</li>
      </ul>
    </section>

    <p class="diy-note">You can also take our products<br>for Do it yourself purpose!</p>

    <p class="tagline">REVOLUTIONIZING STAINLESS CLEANING!</p>
  </main>
</body>
</html>
```